Woman owned consulting company needs an elegant and modern business card design

I need a business card design for my new consulting company, Mira Holcombe Consulting. I am looking for something that is simple and elegant, but also creative and original. You can use either version of the logo that are attached. I have also included the information that needs to be featured on the business card.

Contact Information for Business Card

Requirements
Must have
• The logo and the font type and a standard business card size. Use shades of gray/silver and or rose gold that are in the logo.
• I didn't realize that my actual logo wasn't attached. Please incorporate in the designs.
Should not have
• Colors that are different from my logo

```html
<!DOCTYPE html>
<html lang="en">
<head>
<meta charset="utf-8">
<title>Mira Holcombe Consulting — Business Card</title>
<link href="https://fonts.googleapis.com/css2?family=Cormorant+Garamond:wght@500;600&family=Arimo:wght@400&display=swap" rel="stylesheet">
<style>
  :root {
    --backdrop: #3a3a3c;
    --card-front: #6c6c6c;
    --card-back: #2b2d2d;
    --blush: #f7ece4;
    --silver: #c9cacc;
    --white: #ffffff;
    --rose-line: #d9bfae;
  }
  * { margin: 0; padding: 0; box-sizing: border-box; }
  html, body {
    width: 1200px;
    height: 1200px;
    overflow: hidden;
    background: var(--backdrop);
  }
  .canvas {
    position: relative;
    width: 1200px;
    height: 1200px;
  }
  .card {
    position: absolute;
    left: 180px;
    width: 840px;
    height: 480px;
    border-radius: 28px;
    overflow: hidden;
  }
  .card--front {
    top: 90px;
    background: var(--card-front);
    display: flex;
    align-items: center;
    justify-content: center;
  }
  .card--back {
    top: 630px;
    background: var(--card-back);
  }
  .brand-name {
    font-family: "Cormorant Garamond", serif;
    font-weight: 500;
    color: var(--blush);
    text-align: center;
    line-height: 1.05;
  }
  .card--front .brand-name {
    font-size: 64px;
    letter-spacing: 1px;
  }
  .brand-mark {
    display: flex;
    align-items: center;
    gap: 26px;
  }
  .brand-dot {
    width: 22px;
    height: 22px;
    border-radius: 50%;
    background: var(--blush);
    flex: none;
  }
  .card--back .brand-name {
    position: absolute;
    top: 74px;
    left: 0;
    right: 0;
    font-size: 50px;
    color: var(--silver);
  }
  .contact-block {
    position: absolute;
    right: 60px;
    bottom: 44px;
    text-align: right;
    font-family: "Arimo", sans-serif;
    color: var(--white);
  }
  .person-name {
    font-family: "Cormorant Garamond", serif;
    font-weight: 600;
    font-size: 34px;
    letter-spacing: 1px;
    color: var(--blush);
    line-height: 1;
  }
  .person-role {
    font-size: 19px;
    margin-top: 6px;
  }
  .rule {
    width: 46px;
    height: 2px;
    background: var(--rose-line);
    margin: 14px 0 14px auto;
  }
  .contact-line {
    display: flex;
    align-items: center;
    justify-content: flex-end;
    gap: 14px;
    font-size: 21px;
    line-height: 1;
    margin-top: 10px;
  }
  .contact-line svg {
    width: 24px;
    height: 24px;
    flex: none;
  }
</style>
</head>
<body>
<main class="canvas">
  <section class="card card--front" aria-label="Card front">
    <div class="brand-mark">
      <span class="brand-dot"></span>
      <h1 class="brand-name">Mira Holcombe<br>Consulting</h1>
    </div>
  </section>

  <section class="card card--back" aria-label="Card back">
    <h2 class="brand-name">Mira Holcombe Consulting</h2>

    <div class="contact-block">
      <p class="person-name">MIRA HOLCOMBE</p>
      <p class="person-role">Owner</p>
      <div class="rule"></div>

      <p class="contact-line">610-555-0142
        <svg viewBox="0 0 24 24" fill="none" stroke="#fff" stroke-width="1.8" stroke-linecap="round" stroke-linejoin="round" aria-hidden="true">
          <path d="M5 3h3l2 5-2 1.5a11 11 0 0 0 6.5 6.5L16 14l5 2v3a2 2 0 0 1-2 2A17 17 0 0 1 3 5a2 2 0 0 1 2-2z"/>
        </svg>
      </p>
      <p class="contact-line">mira@miraholcombeconsulting.com
        <svg viewBox="0 0 24 24" fill="none" stroke="#fff" stroke-width="1.8" stroke-linejoin="round" aria-hidden="true">
          <rect x="3" y="5" width="18" height="14" rx="1.5"/>
          <path d="M3 6l9 7 9-7"/>
        </svg>
      </p>
      <p class="contact-line">www.miraholcombeconsulting.com
        <svg viewBox="0 0 24 24" fill="none" stroke="#fff" stroke-width="1.6" aria-hidden="true">
          <circle cx="12" cy="12" r="9"/>
          <ellipse cx="12" cy="12" rx="4" ry="9"/>
          <path d="M3 12h18M5 7h14M5 17h14"/>
        </svg>
      </p>
    </div>
  </section>
</main>
</body>
</html>
```